Business card with logo for a family psychologist

I need a business card for my private practice in the urban Chicago area as a psychologist. I see families and individuals who are going through difficult times - divorce, separation, illness, or trauma. I want to project hopefulness, competence, and caring.

Target Market(s)

Adults, other professionals - such as physicans and lawyers

Industry/Entity Type

Health Care

Contact Information for Business Card

Front should have my name and credentials; back should have location information including my email, phone

Font styles to use
Serif
Decorative
Script

Requirements
Must have
• Unique logo
Should not have
• No pictures or icons of people; no black

```html
<!DOCTYPE html>
<html lang="en">
<head>
<meta charset="utf-8">
<title>Dr. Lena Marsh – Business Card</title>
<link rel="stylesheet" href="https://fonts.googleapis.com/css2?family=Open+Sans:wght@300;400;600&display=swap">
<style>
  :root {
    --canvas-bg: #ece8e2;
    --card-white: #fbfbfb;
    --brand-blue: #14a3c6;
    --brand-blue-light: #22b9db;
    --brand-blue-dark: #0c8cae;
    --text-grey: #7d8a8f;
    --text-dark: #4a5357;
    --on-blue: #ffffff;
  }
  * { margin: 0; padding: 0; box-sizing: border-box; }
  html, body {
    width: 771px;
    height: 1200px;
    overflow: hidden;
    background: var(--canvas-bg);
    font-family: "Open Sans", Arial, sans-serif;
  }
  .canvas {
    position: relative;
    width: 771px;
    height: 1200px;
  }
  .card {
    position: absolute;
    left: 65px;
    width: 641px;
    height: 366px;
    border-radius: 4px;
    box-shadow: 0 6px 18px rgba(60, 50, 40, 0.18);
    overflow: hidden;
  }

  /* Contact side (white) */
  .card--contact {
    top: 150px;
    background: var(--card-white);
  }
  .identity {
    position: absolute;
    left: 42px;
    top: 52px;
    padding-left: 16px;
    border-left: 5px solid var(--brand-blue);
  }
  .identity__name {
    font-weight: 300;
    font-size: 31px;
    line-height: 1.1;
    color: var(--text-grey);
  }
  .identity__title {
    font-weight: 300;
    font-size: 18px;
    line-height: 1.4;
    color: var(--brand-blue);
  }
  .brand {
    position: absolute;
    display: flex;
    align-items: center;
    gap: 10px;
    font-weight: 400;
  }
  .card--contact .brand {
    right: 42px;
    top: 52px;
    font-size: 18px;
    color: var(--brand-blue);
  }
  .brand__square {
    width: 22px;
    height: 22px;
    background: var(--brand-blue);
    border-radius: 4px;
  }
  .contact-list {
    position: absolute;
    left: 300px;
    bottom: 46px;
    list-style: none;
    font-size: 15px;
    color: var(--text-dark);
  }
  .contact-list li {
    display: flex;
    align-items: flex-start;
    gap: 12px;
    margin-top: 10px;
    line-height: 1.45;
  }
  .contact-list svg {
    flex: none;
    width: 14px;
    height: 14px;
    margin-top: 3px;
    fill: var(--brand-blue);
  }

  /* Name side (blue) */
  .card--name {
    top: 684px;
    background: linear-gradient(135deg, var(--brand-blue-light) 0%, var(--brand-blue) 55%, var(--brand-blue-dark) 100%);
    color: var(--on-blue);
  }
  .card--name .brand {
    left: 70px;
    top: 50%;
    transform: translateY(-50%);
    font-size: 24px;
    color: var(--on-blue);
  }
  .card--name .brand__square {
    width: 30px;
    height: 30px;
    background: var(--on-blue);
    border-radius: 6px;
  }
  .feature {
    position: absolute;
    left: 262px;
    top: 50%;
    transform: translateY(-50%);
  }
  .feature__name {
    font-weight: 300;
    font-size: 42px;
    line-height: 1.1;
  }
  .feature__title {
    font-weight: 300;
    font-size: 21px;
    line-height: 1.5;
  }
</style>
</head>
<body>
<main class="canvas">

  <section class="card card--contact" aria-label="Business card contact side">
    <div class="identity">
      <h1 class="identity__name">Dr. Lena Marsh</h1>
      <p class="identity__title">Licensed Clinical Psychologist</p>
    </div>

    <div class="brand">
      <span class="brand__square"></span>
      <span class="brand__name">Marsh Care</span>
    </div>

    <ul class="contact-list">
      <li>
        <svg viewBox="0 0 14 14" aria-hidden="true"><path d="M7 0a5 5 0 0 0-5 5c0 3.6 5 9 5 9s5-5.4 5-9a5 5 0 0 0-5-5zm0 7a2 2 0 1 1 0-4 2 2 0 0 1 0 4z"/></svg>
        <span>240 W. Harlow Ave Suite 310<br>Chicago, Illinois 60610</span>
      </li>
      <li>
        <svg viewBox="0 0 14 14" aria-hidden="true"><path d="M3 1h2.2l1 3-1.4 1.1a8 8 0 0 0 4.1 4.1L10 7.8l3 1V11a2 2 0 0 1-2 2A10 10 0 0 1 1 3a2 2 0 0 1 2-2z"/></svg>
        <span>312-555-0148</span>
      </li>
      <li>
        <svg viewBox="0 0 14 14" aria-hidden="true"><path d="M0 3h14v8H0z M0 3l7 5 7-5" fill="none" stroke="#14a3c6" stroke-width="1.6"/></svg>
        <span>dr.lenamarsh@mailbox.net</span>
      </li>
    </ul>
  </section>

  <section class="card card--name" aria-label="Business card name side">
    <div class="brand">
      <span class="brand__square"></span>
      <span class="brand__name">Marsh Care</span>
    </div>
    <div class="feature">
      <h2 class="feature__name">Dr. Lena Marsh</h2>
      <p class="feature__title">Licensed Clinical Psychologist</p>
    </div>
  </section>

</main>
</body>
</html>
```